Wine labels Velmora Wine Council - Nueva etiqueta El Consejo Regulador de vinos de Albarrán

Velmora Wines Council, based in southern Spain, are looking to create a new suite of wine labels which retain the elegance of the Sherry Wines industry while reinvigorating their image to the modern era and a new generation of Sherry Wine lovers. These labels will be used across the Velmora Wines Council's range of wines for the promotion of the Sherry Wines industry.

Your design must present at least two styles of Sherry Wines which demonstrate an elegant, modern interpretation and understanding of the unique mood and personality for these wines and the essence of southern Spain.

10 labels will be created based on the winning design, one for each of the unique varieties of Sherry Wines within the collection. This collection comprises of several different wine varieties including: Fino, Manzanilla, Amontillado, Oloroso, Palo Cortado, Medium, Cream, Pale Cream, Pedro Ximenez and Moscatel.

We recommend you visit our website www.velmora-vinos.example/wines as the source to understanding the origins and unique personality of these diverse wines.

El Consejo Regulador de los Vinos de Albarrán y Tordesal quiere renovar las etiquetas de los vinos utilizados para sus actividades de promoción genérica. Esta colección de vinos comprende las tipologías más importantes de la región que incluye: fino, manzanilla, amontillado, oloroso, palo cortado, pale cream, medium, cream, pedro ximénez y moscatel. Por lo tanto se precisan 10 etiquetas, una para cada uno de los vinos mencionados.
Updates

Project Deadline Extended
Reason: Due to some confusion with the deadline we wish to officially extend the deadline to allow designers one last week to submit their entries.

Target Market(s)

Industry, journalists, media, sommeliers, chefs, wine writers

Industry/Entity Type

Council

Requirements
Must have
• Front and Back label plus capsule:
• Front label can have either of the two official logos of the Velmora Wine council titled Vinos de Albarrán Digital or not, this is optional. Must include: Vino selecionado por el Consejo Regulador de la Denominacion de Origen, Name of the variety of wine eg FINO, percentage of alcohol eg 15% and quantity 75 cl.
• The back of the label must include the council logo titled Sellora and 4 additional logos positioned smaller. The Europa logo must appear larger than the 3 other logos. Space for descriptive text about the wine is also required.
• The dimensions of the bottle can be found at this link http://www.vidrialto.example/es/catalogo/vinos-y-espumosos/bordelesas/bd-orla
• Altura:305 mm
• Diámetro base:76,20 mm
• Diámetro hombro:82 mm
• Tipo boca:Cetie
• Peso:750 gr
• Capacidad:75 cl
• Etiqueta delantera y trasera y capsula
• La etiqueta delantera puede incluir el logo oficial del Consejo Regulador o el logo digital, o ninguno, esto es opcional. Debe incluir el siguiete texto: Vino selecionado por el Consejo Regulador de la Denominacion de Origen, el nombre de la variedad del vino, por ejemplo Fino, el porcentaje de alcohol, por ejemplo 15%, y la capacidad 75cl.
• La etiqueta trasera debe incluir el logo oficial Sellora del Consejo, y cuatro logos adicionales con una dimension menor. El Logo de ¨Europa invierte en las zonas rurales¨ debe ser de mayor tamaño que los otros. Se precisa espacio para el texto descriptivo de los vinos.
• Las dimensiones de la botella se puede encontrar en este enlace
• http://www.vidrialto.example/es/catalogo/vinos-y-espumosos/bordelesas/bd-orla
• Altura:305 mm
• Diámetro base:76,20 mm
• Diámetro hombro:82 mm
• Tipo boca:Cetie
• Peso:750 gr
• Capacidad:75 cl
Nice to have
• See our website velmora-vinos.example to understand the origin of the wines. Ver nuestra página web velmora-vinos.example para mejor entender los vinos.
Should not have
• Images of catavinos or stereotypical images from Spain such as flamenco dancers or guitars.

```html
<!DOCTYPE html>
<html lang="es">
<head>
<meta charset="utf-8">
<title>Amontillado – Etiqueta delantera</title>
<link rel="stylesheet" href="https://fonts.googleapis.com/css2?family=Bodoni+Moda:wght@400&family=Roboto+Condensed:wght@300;400;700&display=swap">
<style>
  :root {
    --backdrop: #e3e3e3;
    --label-white: #ffffff;
    --ink: #2a2a2a;
    --ink-soft: #8a8a8a;
    --gold: #c9a227;
    --horse-blue: #2f7fd6;
    --horse-green: #3fae4a;
    --horse-lime: #c4dc3a;
    --horse-magenta: #c0238f;
    --horse-violet: #6a3cc2;
  }
  * { margin: 0; padding: 0; box-sizing: border-box; }
  html, body {
    width: 1200px;
    height: 1200px;
    overflow: hidden;
    background: var(--backdrop);
  }
  .front-label {
    position: absolute;
    left: 320px;
    top: 40px;
    width: 560px;
    height: 1120px;
    background: var(--label-white);
    color: var(--ink);
    box-shadow: 0 2px 10px rgba(0,0,0,0.08);
  }
  .council-mark {
    position: absolute;
    top: 70px;
    left: 0;
    width: 100%;
    display: flex;
    flex-direction: column;
    align-items: center;
    gap: 14px;
  }
  .council-mark__square {
    width: 14px;
    height: 14px;
    background: var(--gold);
  }
  .council-mark__name {
    font-family: "Bodoni Moda", serif;
    font-size: 30px;
    line-height: 1.15;
    letter-spacing: 4px;
    text-transform: uppercase;
    text-align: center;
    color: var(--ink);
  }
  .variety-illustration {
    position: absolute;
    left: 70px;
    top: 268px;
    width: 410px;
    height: 462px;
  }
  .variety-name {
    position: absolute;
    top: 770px;
    left: 0;
    width: 100%;
    text-align: center;
    font-family: "Bodoni Moda", serif;
    font-weight: 400;
    font-size: 82px;
    line-height: 1;
    letter-spacing: -1px;
    color: var(--ink);
  }
  .variety-name__initial { color: var(--gold); }
  .selection-note {
    position: absolute;
    top: 888px;
    left: 0;
    width: 100%;
    text-align: center;
    font-family: "Roboto Condensed", sans-serif;
    color: var(--ink-soft);
    font-weight: 300;
    font-size: 19px;
    line-height: 33px;
  }
  .selection-note__council {
    display: block;
    color: var(--ink);
    font-weight: 700;
    font-size: 24px;
  }
  .bottle-facts {
    position: absolute;
    top: 1046px;
    left: 40px;
    right: 35px;
    display: flex;
    justify-content: space-between;
    font-family: "Roboto Condensed", sans-serif;
    font-weight: 300;
    font-size: 37px;
    color: #555555;
  }
</style>
</head>
<body>
  <main class="front-label">
    <div class="council-mark">
      <span class="council-mark__name">Velmora<br>Wine Council</span>
      <span class="council-mark__square"></span>
    </div>

    <svg class="variety-illustration" viewBox="0 0 410 462" role="img" aria-label="Ilustración facetada de un caballo encabritado en colores del arco iris">
      <defs>
        <linearGradient id="horse-tones" x1="0" y1="1" x2="1" y2="0">
          <stop offset="0" stop-color="var(--horse-violet)"/>
          <stop offset="0.3" stop-color="var(--horse-lime)"/>
          <stop offset="0.5" stop-color="var(--horse-green)"/>
          <stop offset="0.75" stop-color="var(--horse-blue)"/>
          <stop offset="1" stop-color="var(--horse-magenta)"/>
        </linearGradient>
      </defs>
      <rect width="410" height="462" rx="6" fill="url(#horse-tones)" opacity="0.85"/>
    </svg>

    <h1 class="variety-name"><span class="variety-name__initial">A</span>montillado</h1>

    <p class="selection-note">
      Vino Seleccionado por el
      <span class="selection-note__council">CONSEJO REGULADOR</span>
      de la Denominación de Origen
    </p>

    <div class="bottle-facts">
      <span class="bottle-facts__alcohol">15% Vol.</span>
      <span class="bottle-facts__volume">75 cl.</span>
    </div>
  </main>
</body>
</html>
```